LABEL DESIGN FOR A NATURAL SKIN CARE LINE

We are looking for a label design for a new natural skin care line that targets the mindfulness and yoga community. We offer a everyday face wash that is derived from natural ingredients and combine it with online yoga classes that will match the intention on the back of the product label. Please make the logo prominent on the front of the bottle, play with horizontal and vertical placement. The product is called “Mellow Rinse”. We like a more modern clean feel.

DERMAVOW is essentially a natural wellness beauty brand that will fuse into a line of products, a design should be versatile and include the colors in the logo along with whites. The final design should communicate a natural feel that will speak to the yoga community and mindfulness movement.

Target Market(s)

Yogis, fitness community, natural products

Industry/Entity Type

Skin Care Product

Font styles to use
Serif
Decorative

Requirements
Must have
• logo on the front that is prominent, with “MELLOW RINSE” as the product name.

Bottle Dimensions:
3OZ 3.35x4.75in (check attachments)
Nice to have
• Unique designs that stand out. Use the colors in logo. Would be great to have a third eye as a watermark
Should not have
• dark colors,

```html
<!DOCTYPE html>
<html lang="en">
<head>
<meta charset="utf-8">
<title>DERMAVOW Mellow Rinse Face Wash Label</title>
<link href="https://fonts.googleapis.com/css2?family=Josefin+Sans:wght@300;400;600&display=swap" rel="stylesheet">
<style>
  :root {
    --page-bg: #f1f1f0;
    --label-bg: #fbfbfb;
    --brand-green: #38a85e;
    --brand-teal: #1f9a8c;
    --ink-dark: #3d3d3d;
    --ink-mid: #555555;
    --swirl-tone: #e4e4e4;
  }
  * { margin: 0; padding: 0; box-sizing: border-box; }
  html, body {
    width: 1200px;
    height: 1200px;
    overflow: hidden;
    background: var(--page-bg);
    font-family: "Josefin Sans", sans-serif;
  }
  .canvas {
    width: 1200px;
    height: 1200px;
    display: flex;
    align-items: center;
    justify-content: center;
  }
  .label {
    position: relative;
    width: 600px;
    height: 850px;
    background: var(--label-bg);
    box-shadow: 0 2px 14px rgba(0,0,0,0.06);
    text-align: center;
    overflow: hidden;
  }
  .label__watermark {
    position: absolute;
    left: 120px;
    top: 330px;
    width: 360px;
    height: 360px;
    border-radius: 50%;
    background: radial-gradient(circle, rgba(228,228,228,0) 30%, var(--swirl-tone) 55%, rgba(228,228,228,0) 72%);
  }
  .brand {
    position: absolute;
    top: 70px;
    left: 0;
    width: 100%;
  }
  .brand__mark {
    display: block;
    margin: 0 auto 26px;
    width: 110px;
    height: 110px;
  }
  .brand__name {
    font-weight: 400;
    font-size: 58px;
    letter-spacing: 2px;
    color: var(--brand-green);
  }
  .product {
    position: absolute;
    top: 440px;
    left: 0;
    width: 100%;
    color: var(--ink-dark);
  }
  .product__first {
    font-weight: 300;
    font-size: 54px;
    letter-spacing: 1px;
    line-height: 1;
  }
  .product__second {
    font-weight: 600;
    font-size: 74px;
    letter-spacing: 1px;
    line-height: 1.1;
  }
  .product__type {
    margin-top: 14px;
    font-weight: 400;
    font-size: 24px;
    letter-spacing: 4px;
    color: var(--ink-mid);
  }
  .specs {
    position: absolute;
    top: 725px;
    left: 0;
    width: 100%;
    font-weight: 600;
    font-size: 18px;
    letter-spacing: 3px;
    line-height: 1.5;
    color: var(--ink-dark);
  }
  .label__band {
    position: absolute;
    left: 200px;
    bottom: 0;
    width: 200px;
    height: 52px;
    background: var(--brand-teal);
  }
</style>
</head>
<body>
  <main class="canvas">
    <section class="label">
      <div class="label__watermark" role="img" aria-label="Faint grey swirl watermark behind the product name"></div>

      <header class="brand">
        <svg class="brand__mark" viewBox="0 0 110 110" aria-hidden="true">
          <circle cx="55" cy="55" r="50" fill="none" stroke="var(--brand-green)" stroke-width="4"/>
        </svg>
        <div class="brand__name">DERMAVOW</div>
      </header>

      <div class="product">
        <div class="product__first">MELLOW</div>
        <div class="product__second">RINSE</div>
        <div class="product__type">FACE WASH</div>
      </div>

      <div class="specs">
        <div class="specs__skin">ALL SKIN TYPES</div>
        <div class="specs__size">3OZ</div>
      </div>

      <div class="label__band"></div>
    </section>
  </main>
</body>
</html>
```